Talvenridge

We are re-branding the company with a new logo (attached) which I would
like to go on one side of the card, and I have attached a file showing what
the old back side looked like, and I do like the characters that show the
phone, e-mails, etc., I don't like the current arrangement, and I want
something clean, clear and out of the box, as we are an aviation consulting
firm, and we work outside of the box.

```html
<!DOCTYPE html>
<html lang="en">
<head>
<meta charset="utf-8">
<title>Talvenridge Business Card</title>
<link href="https://fonts.googleapis.com/css2?family=Lato:wght@400;700;900&display=swap" rel="stylesheet">
<style>
  :root {
    --backdrop: #2b2b2d;
    --card: #f7f7f7;
    --red: #c8161d;
    --red-dark: #9c1016;
    --ink: #3a3a3c;
    --muted: #8c8c8e;
  }
  * { margin: 0; padding: 0; box-sizing: border-box; }
  html, body { width: 1200px; height: 900px; overflow: hidden; }
  body {
    background: var(--backdrop);
    font-family: "Lato", sans-serif;
    position: relative;
  }
  .card {
    position: absolute;
    width: 640px;
    height: 366px;
    background: var(--card);
    overflow: hidden;
    box-shadow: 0 14px 30px rgba(0,0,0,0.45);
  }
  .card-front { left: 60px; top: 60px; }
  .card-back { left: 500px; top: 474px; }
  .card-bands { position: absolute; inset: 0; width: 100%; height: 100%; }

  .brand { display: flex; align-items: center; gap: 12px; }
  .brand-dot {
    width: 30px; height: 30px; border-radius: 50%;
    background: var(--red);
  }
  .brand-name {
    font-weight: 900;
    font-size: 44px;
    color: var(--ink);
    letter-spacing: 1px;
    line-height: 1;
  }
  .tagline {
    font-size: 13px;
    color: var(--muted);
    letter-spacing: 0.5px;
    margin-top: 4px;
  }
  .tagline .sep { color: var(--red); }

  /* front */
  .front-content {
    position: absolute;
    left: 0; right: 0; top: 74px;
    display: flex; flex-direction: column; align-items: center;
  }
  .web-pill {
    margin-top: 12px;
    background: var(--red);
    color: #fff;
    font-size: 15px;
    padding: 4px 16px;
    border-radius: 14px;
    letter-spacing: 0.5px;
  }
  .services {
    margin-top: 30px;
    text-align: center;
    color: var(--red);
    font-weight: 700;
    font-size: 18px;
    line-height: 1.45;
  }

  /* back */
  .back-brand { position: absolute; left: 48px; top: 86px; }
  .back-brand .brand-name { font-size: 38px; }
  .person { position: absolute; right: 40px; top: 66px; text-align: right; }
  .person-name { font-weight: 900; color: var(--red); font-size: 21px; }
  .person-role { font-weight: 700; color: var(--ink); font-size: 14px; margin-top: 2px; }
  .contacts { position: absolute; list-style: none; font-size: 17px; color: var(--ink); }
  .contacts li { display: flex; align-items: flex-start; gap: 10px; margin-bottom: 10px; line-height: 1.3; }
  .contacts svg { width: 18px; height: 18px; flex-shrink: 0; margin-top: 2px; fill: var(--ink); }
  .contacts-phone { left: 120px; top: 226px; }
  .contacts-reach { left: 350px; top: 172px; }
</style>
</head>
<body>

<section class="card card-front">
  <svg class="card-bands" viewBox="0 0 640 366" preserveAspectRatio="none" aria-hidden="true">
    <path d="M0 0 H170 C150 0 145 14 132 14 H14 V366 H0 Z" fill="var(--red)"/>
    <path d="M640 366 H230 C250 366 262 330 290 330 H626 V0 H640 Z" fill="var(--red)"/>
  </svg>
  <div class="front-content">
    <div class="brand">
      <span class="brand-dot"></span>
      <span class="brand-name">Talvenridge</span>
    </div>
    <p class="tagline">trusted experience <span class="sep">•</span> proven solutions</p>
    <p class="web-pill">www.talvenridge.aero</p>
    <p class="services">Aircraft Finances &amp; Leasing / Technical Services<br>Aviation consulting / Airline restructuring</p>
  </div>
</section>

<section class="card card-back">
  <svg class="card-bands" viewBox="0 0 640 366" preserveAspectRatio="none" aria-hidden="true">
    <path d="M130 0 H640 V12 H170 C150 12 145 28 120 28 C125 20 125 0 130 0 Z" fill="var(--red)"/>
    <path d="M0 366 H640 V352 C620 352 610 316 585 316 H0 Z" fill="var(--red)"/>
  </svg>
  <div class="back-brand">
    <div class="brand">
      <span class="brand-dot"></span>
      <span class="brand-name">Talvenridge</span>
    </div>
    <p class="tagline">trusted experience <span class="sep">•</span> proven solutions</p>
  </div>
  <div class="person">
    <p class="person-name">YOUR NAME</p>
    <p class="person-role">Designation</p>
  </div>
  <ul class="contacts contacts-phone">
    <li><svg viewBox="0 0 24 24"><path d="M2 9c0-3 4-5 10-5s10 2 10 5v2h-5V8c-1-.6-3-1-5-1s-4 .4-5 1v3H2z M6 12h12l3 8H3z"/></svg>+1 555 214 0368</li>
    <li><svg viewBox="0 0 24 24"><path d="M7 1h10a2 2 0 0 1 2 2v18a2 2 0 0 1-2 2H7a2 2 0 0 1-2-2V3a2 2 0 0 1 2-2zm0 3v15h10V4z"/></svg>+1 555 730 4192</li>
  </ul>
  <ul class="contacts contacts-reach">
    <li><svg viewBox="0 0 24 24"><path d="M2 5h20v14H2z M3 6l9 7 9-7" stroke="#f7f7f7" stroke-width="1.5"/></svg>mk@talvenridge.aero</li>
    <li><svg viewBox="0 0 24 24"><path d="M12 2l11 10h-3v10h-6v-6h-4v6H4V12H1z"/></svg>420B Larkspur Lane,<br>Fairhaven, CA 90017</li>
  </ul>
</section>

</body>
</html>
```